Eye catching business card

2 sided
Black background with logo in color on one side along with the words "Proudly serving the commercial and defense industries since 1975"
2nd side to contain contact information (see attached current business card) and "Waterjet, Composite, Precision Machining and Clean Room Manufacturing" with a very faint watermark of a waving USA Flag in the back ground.
Remove the "est. 195" from the current logo design

```html
<!DOCTYPE html>
<html lang="en">
<head>
<meta charset="utf-8">
<title>Vanguard Machine Inc — Business Card</title>
<link href="https://fonts.googleapis.com/css2?family=Michroma&family=Cinzel:wght@500&display=swap" rel="stylesheet">
<style>
  :root {
    --ink: #231f20;
    --paper: #ffffff;
    --steel: #8a8d91;
    --sky: #1ea7e8;
    --sky-pale: #bfe7fb;
    --stage: #e9eaec;
    --watermark: #f2f3f5;
    --divider: #c9cbce;
  }
  html, body {
    margin: 0;
    width: 1200px;
    height: 891px;
    overflow: hidden;
    background: var(--stage);
  }
  .sheet {
    position: relative;
    width: 1200px;
    height: 891px;
  }
  .card {
    position: absolute;
    top: 291px;
    width: 540px;
    height: 309px;
    box-shadow: 0 8px 24px rgba(0,0,0,.18);
  }
  .card--front { left: 40px; }
  .card--back { left: 620px; }
  .card svg { display: block; }
  .brand-name {
    font-family: "Michroma", sans-serif;
    fill: var(--steel);
  }
  .tagline {
    font-family: "Cinzel", serif;
    fill: var(--sky);
    font-size: 7px;
  }
  .contact {
    font-family: "Michroma", sans-serif;
    fill: var(--ink);
  }
</style>
</head>
<body>
<main class="sheet">

  <!-- Front side -->
  <section class="card card--front" aria-label="Card front">
    <svg width="540" height="309" viewBox="0 0 540 309">
      <defs>
        <linearGradient id="bandFront" x1="0" y1="0" x2="1" y2="1">
          <stop offset="0" stop-color="var(--sky)"/>
          <stop offset="1" stop-color="var(--sky-pale)"/>
        </linearGradient>
      </defs>
      <rect width="540" height="309" fill="var(--ink)"/>
      <!-- lower-left band -->
      <polygon points="0,100 0,309 300,309" fill="url(#bandFront)"/>
      <polygon points="0,88 318,309 300,309 0,100" fill="var(--paper)"/>
      <!-- right corner band -->
      <polygon points="430,0 540,0 540,150" fill="url(#bandFront)"/>
      <polygon points="420,0 430,0 540,150 540,162" fill="var(--paper)"/>

      <!-- brand -->
      <circle cx="180" cy="144" r="10" fill="var(--sky)"/>
      <text class="brand-name" x="198" y="151" font-size="17">VANGUARD MACHINE INC</text>
      <line x1="198" y1="164" x2="478" y2="164" stroke="var(--steel)" stroke-width="1.5"/>

      <text class="tagline" transform="translate(12 91) rotate(34.8)" textLength="340" lengthAdjust="spacing">PROUDLY SERVING THE COMMERCIAL AND DEFENSE INDUSTRIES SINCE 1975</text>
    </svg>
  </section>

  <!-- Back side -->
  <section class="card card--back" aria-label="Card back">
    <svg width="540" height="309" viewBox="0 0 540 309">
      <defs>
        <linearGradient id="bandBack" x1="0" y1="0" x2="1" y2="0">
          <stop offset="0" stop-color="var(--sky)"/>
          <stop offset="1" stop-color="var(--paper)"/>
        </linearGradient>
      </defs>
      <rect width="540" height="309" fill="var(--paper)"/>
      <!-- flag watermark area -->
      <rect x="250" y="96" width="120" height="88" fill="var(--watermark)" role="img" aria-label="Very faint waving flag watermark"/>
      <!-- corner blocks -->
      <polygon points="0,100 0,309 260,309" fill="var(--ink)"/>
      <polygon points="230,262 540,262 540,309 262,309" fill="url(#bandBack)" opacity=".85"/>
      <polygon points="0,92 272,309 262,309 0,100" fill="var(--divider)"/>

      <!-- brand -->
      <circle cx="40" cy="64" r="9" fill="var(--sky)"/>
      <text class="brand-name" x="56" y="70" font-size="14">VANGUARD MACHINE INC</text>
      <line x1="56" y1="80" x2="312" y2="80" stroke="var(--steel)" stroke-width="1"/>

      <!-- person -->
      <text class="contact" x="512" y="62" font-size="11" text-anchor="end">DALE MORGAN</text>
      <text class="contact" x="512" y="74" font-size="6" text-anchor="end">PRESIDENT</text>
      <line x1="380" y1="80" x2="512" y2="80" stroke="var(--steel)" stroke-width="1"/>
      <text class="contact" x="512" y="94" font-size="6" text-anchor="end">OFFICE 555-010-0008</text>
      <text class="contact" x="512" y="106" font-size="6" text-anchor="end">DALE@VANGUARDMACH.COM</text>

      <!-- company -->
      <text class="contact" x="512" y="198" font-size="6.5" text-anchor="end">VANGUARD MACHINE INC.</text>
      <text class="contact" x="512" y="210" font-size="6.5" text-anchor="end">WATERJETS, COMPOSITES &amp; PRECISION MACHINING</text>
      <text class="contact" x="512" y="222" font-size="6.5" text-anchor="end">120 MILL CREEK RD. FAIRVIEW, PA 17000</text>
      <text class="contact" x="512" y="238" font-size="6.5" text-anchor="end">• PHONE: 555-010-0008 • FAX 555-010-0010</text>
      <text class="contact" x="512" y="250" font-size="6.5" text-anchor="end">INFO@VANGUARDMACH.COM • WWW.VANGUARDMACH.COM</text>
    </svg>
  </section>

</main>
</body>
</html>
```